Heater product information sheets

I need the two product information sheets organized and laid out in a clean, easy to read attractive manner. These sheets are to advertise propane heaters for outdoor use and for wholesale to propane distributors, restaurants and homeowners that need to have propane heat as the winter ends and spring begins. They will be used for chilly evenings when people want to be outside eating, drinking and being social.
Updates

Low design quality

Target Market(s)

Restaurants, hospitality industry, special events, party rental companies, home owners with backyards

Font styles to use
Sans Serif

Requirements
Must have
• My logo in the document instead of k. Dahlby and company
Nice to have
• I would like to see Fire illustrated coming up the heaters and on the round glass, show it up the middle of the glass tube propane heater.

```html
<!DOCTYPE html>
<html lang="en">
<head>
<meta charset="utf-8">
<title>Outdoor Propane Heater – Product Sheet</title>
<link rel="stylesheet" href="https://fonts.googleapis.com/css2?family=Abril+Fatface&family=Lato:wght@400;700&family=Montserrat:ital,wght@0,700;0,800;1,700;1,800&family=PT+Sans+Narrow:wght@700&display=swap">
<style>
  :root {
    --page-bg: #e6e6e6;
    --sheet-white: #fdfdfd;
    --flame-orange: #d67e27;
    --warm-yellow: #f8c862;
    --label-yellow: #f6c24f;
    --ink: #111111;
    --metal-light: #b9b9b9;
    --metal-dark: #141414;
  }
  * { box-sizing: border-box; margin: 0; padding: 0; }
  html, body { width: 1200px; height: 960px; overflow: hidden; background: var(--page-bg); }
  .sheet {
    position: absolute; left: 244px; top: 20px;
    width: 712px; height: 920px;
    background: var(--sheet-white);
    overflow: hidden;
    box-shadow: 0 4px 18px rgba(0,0,0,0.18);
    font-family: "Lato", sans-serif; color: var(--ink);
  }
  .sheet-shapes { position: absolute; inset: 0; }
  .product-photo {
    position: absolute; left: 105px; top: 62px; width: 160px; height: 440px;
    border-radius: 80px 80px 14px 14px;
    background: linear-gradient(180deg, var(--metal-light) 0%, #8e8e8e 28%, #555 45%, var(--metal-dark) 70%, #000 100%);
  }
  .uses {
    position: absolute; left: 305px; top: 70px;
    list-style: none;
    font-family: "Montserrat", sans-serif; font-weight: 800; font-style: italic;
    font-size: 15px; line-height: 23px; text-transform: uppercase;
  }
  .uses li::before { content: "• "; }
  .info-col { position: absolute; top: 158px; }
  .info-col.specs { left: 305px; width: 165px; }
  .info-col.details { left: 486px; width: 210px; border-left: 1px solid #333; padding-left: 12px; top: 152px; height: 232px; }
  .col-label {
    display: inline-block; background: var(--label-yellow);
    font-family: "Montserrat", sans-serif; font-weight: 800; font-size: 13.5px;
    letter-spacing: 1.2px; padding: 1px 5px; margin-bottom: 7px;
  }
  .info-col ul { list-style: none; font-size: 11.2px; line-height: 16.5px; }
  .info-col li { padding-left: 11px; position: relative; }
  .info-col li::before { content: "•"; position: absolute; left: 0; }
  .product-title {
    position: absolute; left: 128px; top: 548px;
    font-family: "Abril Fatface", serif; color: #fff;
    font-size: 78px; line-height: 74px; letter-spacing: 1px;
  }
  .order-block { position: absolute; left: 158px; top: 812px; width: 240px; }
  .order-lead {
    font-family: "Montserrat", sans-serif; font-style: italic; font-weight: 700;
    font-size: 13px; letter-spacing: 3px; margin-bottom: 5px; white-space: nowrap;
  }
  .company-name {
    display: inline-block; background: var(--flame-orange); color: #fff;
    font-family: "PT Sans Narrow", sans-serif; font-weight: 700;
    font-size: 22px; padding: 2px 8px; letter-spacing: 0.3px; white-space: nowrap;
  }
  .contact {
    position: absolute; left: 414px; top: 810px; width: 286px;
    border-bottom: 1px solid #333; padding-bottom: 5px;
    font-size: 13.5px; line-height: 22px; font-style: normal;
  }
  .contact-row { display: flex; align-items: center; gap: 6px; white-space: nowrap; }
  .contact-row .sep { width: 6px; flex: none; }
  .contact-icon { width: 14px; height: 14px; flex: none; }
  .note {
    position: absolute; left: 158px; top: 886px;
    font-family: "PT Sans Narrow", sans-serif; font-size: 12.5px; white-space: nowrap;
  }
  .note-label { color: var(--flame-orange); font-size: 15px; font-weight: 700; margin-right: 4px; }
</style>
</head>
<body>
<article class="sheet">
  <svg class="sheet-shapes" viewBox="0 0 712 920" width="712" height="920" aria-hidden="true">
    <path d="M0,822 C300,832 600,700 712,455 L712,920 L0,920 Z" fill="var(--warm-yellow)"/>
    <path d="M0,592 C80,532 160,500 262,510 C382,524 500,520 556,452 C562,602 472,762 250,776 C130,783 50,764 0,748 Z" fill="var(--flame-orange)"/>
  </svg>

  <div class="product-photo" role="img" aria-label="Photo of a tall black patio heater with a round silver reflector top"></div>

  <ul class="uses">
    <li>Rentals for live events</li>
    <li>Rentals for restaurants &amp; catering halls</li>
    <li>Purchase for your home or business</li>
  </ul>

  <section class="info-col specs">
    <h2 class="col-label">SPECIFICATIONS</h2>
    <ul>
      <li>Powerful 48,000 BTU</li>
      <li>Black Powder Coated Finish</li>
      <li>Uses 20 lbs. Propane Tank</li>
      <li>CE, GS, AGA, CSA, with ETL certificate and ROHS approved.</li>
    </ul>
  </section>

  <section class="info-col details">
    <h2 class="col-label">ADDITIONAL DETAILS</h2>
    <ul>
      <li>Commercial Quality</li>
      <li>For Outdoor Use Only</li>
      <li>Conforms to ANSI STD Z83.26-2014 Certified to CSA STD 2.37-2014 Gas-fired outdoor infrared patio heaters</li>
      <li>Safety Auto Shut Off Switch</li>
      <li>Thermostatic Control</li>
      <li>Base Diameter 17” - Anti-Tip Design</li>
      <li>Standard Wheels - Tilt &amp; Move</li>
      <li>Run time: 8-10 hours with standard 20 lbs. Propane tank</li>
      <li>88” Tall</li>
      <li>Heating Area: 200 sq. ft</li>
    </ul>
  </section>

  <h1 class="product-title">Outdoor<br>Propane<br>Heater</h1>

  <div class="order-block">
    <p class="order-lead">To Rent or Purchase:</p>
    <p class="company-name">K. DAHLBY AND COMPANY</p>
  </div>

  <address class="contact">
    <div class="contact-row">
      <svg class="contact-icon" viewBox="0 0 14 14" aria-hidden="true"><circle cx="7" cy="7" r="7" fill="var(--flame-orange)"/><path d="M4.5,3.6 l1.3,-0.3 0.8,1.8 -0.9,0.7 c0.4,1 1.1,1.8 2.1,2.3 l0.7,-0.9 1.8,0.8 -0.3,1.3 c-3,0.2 -5.7,-2.6 -5.5,-5.7z" fill="#fff"/></svg>
      <span>555-214-3870</span>
      <span class="sep"></span>
      <svg class="contact-icon" viewBox="0 0 14 14" aria-hidden="true"><circle cx="7" cy="7" r="7" fill="var(--flame-orange)"/><rect x="3.5" y="4.5" width="7" height="5" fill="#fff"/><path d="M3.5,4.5 L7,7.3 L10.5,4.5" stroke="var(--flame-orange)" stroke-width="0.9" fill="none"/></svg>
      <span>hi@kdahlbyrental.com</span>
    </div>
    <div class="contact-row">
      <svg class="contact-icon" viewBox="0 0 14 14" aria-hidden="true"><circle cx="7" cy="7" r="7" fill="var(--flame-orange)"/><path d="M7,2.8 a2.8,2.8 0 0 1 2.8,2.8 c0,2 -2.8,5 -2.8,5 s-2.8,-3 -2.8,-5 a2.8,2.8 0 0 1 2.8,-2.8z" fill="#fff"/><circle cx="7" cy="5.6" r="1" fill="var(--flame-orange)"/></svg>
      <span>42 Millbrook Lane Ashford, NJ 07000</span>
    </div>
  </address>

  <p class="note"><span class="note-label">NOTE</span>• Price: Starting at $250 each &nbsp;• Assembly &amp; Delivery available upon request &nbsp;• Discounts for large quantity orders</p>
</article>
</body>
</html>
```